Business card (AI file uploaded)

We need a business card design that is minimalist using existing logo (attached). Source files must be editable so we can make the same design with other names.

Screenshots included of a design I was working on to give you an idea of the style I would like. Looking for similar modern styles

Thanks

```html
<!DOCTYPE html>
<html lang="en">
<head>
<meta charset="utf-8">
<title>Marlow Law Group – Business Card</title>
<link rel="stylesheet" href="https://fonts.googleapis.com/css2?family=Open+Sans:wght@400;600&display=swap">
<style>
  :root {
    --stage: #e9e6e1;
    --card-dark: #1c1c1e;
    --card-dark-edge: #2b2b2e;
    --card-light: #ffffff;
    --ink: #1e1e1e;
    --ink-soft: #555555;
    --on-dark: #f2f2f2;
    --on-dark-soft: #cfcfcf;
    --mark-faint: #ececec;
  }
  * { box-sizing: border-box; margin: 0; padding: 0; }
  html, body { width: 1200px; height: 784px; overflow: hidden; }
  body {
    background: var(--stage);
    font-family: "Open Sans", Arial, sans-serif;
    position: relative;
  }
  .card {
    position: absolute;
    width: 560px;
    height: 320px;
    border-radius: 4px;
    box-shadow: 0 10px 28px rgba(0,0,0,.22);
    overflow: hidden;
  }
  /* Front */
  .card--front {
    left: 130px; top: 80px;
    background: radial-gradient(ellipse at 50% 35%, var(--card-dark-edge), var(--card-dark) 75%);
    color: var(--on-dark);
    text-align: center;
  }
  .brand {
    display: flex; flex-direction: column; align-items: center;
    font-weight: 600;
  }
  .brand__dot {
    width: 48px; height: 48px; border-radius: 50%;
    margin-bottom: 14px;
  }
  .brand__name { font-size: 38px; letter-spacing: 1px; line-height: 1; }
  .brand__sub { font-size: 15px; letter-spacing: 4px; margin-top: 4px; }
  .card--front .brand { margin-top: 42px; }
  .card--front .brand__dot { background: var(--on-dark); }
  .services {
    position: absolute; left: 0; right: 0; bottom: 40px;
    font-size: 14px; letter-spacing: 2px; color: var(--on-dark-soft);
  }
  /* Back */
  .card--back {
    left: 510px; top: 370px;
    background: var(--card-light);
    color: var(--ink);
  }
  .card--back .brand {
    position: absolute; left: 40px; top: 30px;
    align-items: flex-start; color: var(--ink);
  }
  .card--back .brand__dot { background: var(--ink); margin-left: 22px; }
  .card--back .brand__name { font-size: 34px; }
  .card--back .brand__sub { font-size: 13px; }
  .decor-circle {
    position: absolute; right: -60px; top: 60px;
    width: 250px; height: 250px; border-radius: 50%;
    border: 14px solid var(--mark-faint);
  }
  .contact {
    position: absolute; left: 40px; bottom: 30px;
    font-size: 14px; line-height: 1.45;
  }
  .contact__name { font-size: 19px; font-weight: 600; line-height: 1.2; }
  .contact__title { font-size: 12px; color: var(--ink-soft); margin-bottom: 12px; }
  .contact b { font-weight: 600; }
</style>
</head>
<body>
  <section class="card card--front">
    <div class="brand">
      <span class="brand__dot"></span>
      <span class="brand__name">MARLOW</span>
      <span class="brand__sub">LAW GROUP</span>
    </div>
    <p class="services">Real | Estate | Bankruptcy | Social Security Disability</p>
  </section>

  <section class="card card--back">
    <span class="decor-circle"></span>
    <div class="brand">
      <span class="brand__dot"></span>
      <span class="brand__name">MARLOW</span>
      <span class="brand__sub">LAW GROUP</span>
    </div>
    <div class="contact">
      <p class="contact__name">Daniel Marlow</p>
      <p class="contact__title">Attorney At Law</p>
      <p>410 Harbor Ave., Suite 200, Lakeview IL 60611</p>
      <p><b>P:</b>555.014.2870 &nbsp;<b>F:</b>555.014.2871</p>
      <p>dmarlow@marlowlaw.com</p>
    </div>
  </section>
</body>
</html>
```